Independent Financial Advisor Billboard Campaign - Maple Ridge Financial

I am a local, independent financial advisor. My company is Maple Ridge Financial, located in Charleston, WV. My main source of revenue comes from those nearing or entering retirement that need assistance with financial planning and investment management. Many are looking to rollover their employer retirement plan into an IRA account. I would like a billboard design campaign that focuses on this type of client. Please see our website www.mapleridgefinancial-example.com for more information.

```html
<!DOCTYPE html>
<html lang="en">
<head>
<meta charset="utf-8">
<title>Maple Ridge Financial – Billboard</title>
<link rel="stylesheet" href="https://fonts.googleapis.com/css2?family=Archivo+Black&family=Archivo:wght@700;800&family=Fira+Sans:wght@500&display=swap">
<style>
  :root {
    --backdrop: #454545;
    --navy-deep: #06237a;
    --navy: #0b2f9a;
    --navy-bright: #1640b4;
    --ink: #0a2a7e;
    --silver-mid: #c9ccd2;
    --lime: #a8dc00;
    --white: #ffffff;
  }
  * { margin: 0; padding: 0; box-sizing: border-box; }
  html, body { width: 1054px; height: 1200px; overflow: hidden; }
  body { background: var(--backdrop); position: relative; }

  .billboard {
    position: absolute; left: 27px; top: 433px;
    width: 1000px; height: 333px; overflow: hidden;
    background: radial-gradient(ellipse at 45% 45%, var(--navy-bright) 0%, var(--navy) 45%, var(--navy-deep) 100%);
  }
  .band-svg { position: absolute; left: 0; top: 0; }

  .headline {
    position: absolute; left: 383px; right: 30px; top: 12px;
    text-align: center;
    font-family: "Archivo Black", sans-serif;
    font-size: 38px; line-height: 44px; letter-spacing: 0.2px;
    color: var(--ink);
  }

  .advisor-photo {
    position: absolute; left: 3px; top: 11px; width: 274px; height: 267px;
    border-radius: 120px 120px 0 0;
    background: linear-gradient(180deg, #d9b49c 0%, #cfa58c 35%, #eef0f4 55%, #dfe2e8 100%);
  }

  .brand {
    position: absolute; left: 310px; top: 104px; right: 30px; height: 56px;
    display: flex; align-items: center; justify-content: center; gap: 18px;
  }
  .brand-mark {
    flex: none; width: 48px; height: 48px;
    background: var(--silver-mid);
  }
  .brand-name {
    font-family: "Archivo", sans-serif; font-weight: 800;
    font-size: 40px; line-height: 48px; letter-spacing: 0.5px;
    color: var(--white); white-space: nowrap;
  }

  .services {
    position: absolute; left: 288px; top: 205px; right: 20px; height: 50px;
    list-style: none;
  }
  .service {
    position: absolute; top: 0; display: flex; align-items: center; gap: 10px;
    font-family: "Archivo", sans-serif; font-weight: 800;
    font-size: 18px; line-height: 20px; color: var(--white); text-transform: uppercase;
  }
  .service svg { flex: none; fill: none; stroke: var(--lime); stroke-width: 1.6; stroke-linejoin: round; stroke-linecap: round; }
  .service--retirement { left: 0; top: 8px; }
  .service--college { left: 192px; top: 6px; }
  .service--estate { left: 365px; top: 0; }
  .service--advice { left: 543px; top: 0; }

  .phone {
    position: absolute; left: 35px; top: 282px;
    font-family: "Archivo Black", sans-serif; font-size: 39px; line-height: 48px;
    color: var(--ink); letter-spacing: 0.5px;
  }
  .website {
    position: absolute; left: 420px; right: 30px; top: 286px;
    text-align: center;
    font-family: "Fira Sans", sans-serif; font-weight: 500; font-size: 29px; line-height: 40px;
    color: var(--ink); letter-spacing: 0.3px;
  }
</style>
</head>
<body>
  <section class="billboard">
    <svg class="band-svg" width="1000" height="333" viewBox="0 0 1000 333">
      <defs>
        <linearGradient id="silver-sheen" x1="0" y1="0" x2="1" y2="0">
          <stop offset="0" stop-color="#a9adb4"/>
          <stop offset="0.25" stop-color="#f4f5f7"/>
          <stop offset="0.5" stop-color="#d0d3d8"/>
          <stop offset="0.75" stop-color="#f7f8f9"/>
          <stop offset="1" stop-color="#a3a7ae"/>
        </linearGradient>
        <linearGradient id="silver-left" x1="0" y1="0" x2="1" y2="0">
          <stop offset="0" stop-color="#d7dade"/>
          <stop offset="0.35" stop-color="#f5f6f8"/>
          <stop offset="1" stop-color="#9ca0a8"/>
        </linearGradient>
      </defs>
      <polygon class="headline-band" points="317,0 1000,0 1000,67 383,67" fill="url(#silver-sheen)"/>
      <polygon class="contact-band" points="0,278 378,278 416,333 0,333" fill="url(#silver-left)"/>
      <polygon class="divider-stripe" points="378,278 392,278 430,333 416,333" fill="var(--navy-deep)"/>
      <polygon class="web-band" points="392,278 1000,278 1000,333 430,333" fill="var(--lime)"/>
    </svg>

    <div class="headline">RETIREMENT DONE RIGHT</div>

    <div class="advisor-photo" role="img" aria-label="Portrait photo of the financial advisor in a white polo shirt"></div>

    <div class="brand">
      <div class="brand-mark" aria-hidden="true"></div>
      <div class="brand-name">MAPLE RIDGE FINANCIAL</div>
    </div>

    <ul class="services">
      <li class="service service--retirement">
        <svg width="42" height="38" viewBox="0 0 42 38">
          <path d="M12 12 A12 7 0 0 1 36 12 Z"/>
          <path d="M24 5 V24"/>
          <path d="M3 30 L28 30 L37 22"/>
          <path d="M6 30 L4 36 M25 30 L27 36"/>
        </svg>
        <span>Retirement<br>Planning</span>
      </li>
      <li class="service service--college">
        <svg width="40" height="42" viewBox="0 0 40 42">
          <path d="M3 14 L20 3 L37 14 Z"/>
          <circle cx="20" cy="10" r="2"/>
          <path d="M5 17 H35 M8 17 V32 M16 17 V32 M24 17 V32 M32 17 V32"/>
          <path d="M4 35 H36 M2 39 H38"/>
        </svg>
        <span>College<br>Planning</span>
      </li>
      <li class="service service--estate">
        <svg width="40" height="42" viewBox="0 0 40 42">
          <path d="M14 3 H36 C34 10 30 18 30 30 C30 36 27 39 23 39 H6 C3 39 2 36 4 33 C8 27 11 14 14 3 Z"/>
          <circle cx="28" cy="35" r="3"/>
        </svg>
        <span>Estate<br>Planning</span>
      </li>
      <li class="service service--advice">
        <svg width="40" height="34" viewBox="0 0 40 34">
          <path d="M2 4 H14 L17 8 H38 V32 H2 Z"/>
          <path d="M2 12 H38"/>
          <circle cx="20" cy="22" r="6"/>
          <path d="M20 18 V25 M17 22 L20 25 L23 22"/>
        </svg>
        <span>Helpful<br>Advice</span>
      </li>
    </ul>

    <div class="phone">304.555.0142</div>
    <div class="website">www.mapleridgefinancial-example.com</div>
  </section>
</body>
</html>
```